New web design for software product company

Our company, Tracvenna, does big data analytics for system monitoring and root cause analysis. We help large enterprise IT organisations improve service levels and increase efficiency through searching, analysing and visualising log data.

We need a new design for www.tracvenna-example.com.

The primary goal of the site is to drive visitors to download our product.

We are launching a new 2.0 version of our product in mid-July. In addition to updating our web design, we will need to replace all of the current product images on the current site. We have attached several sample images of the new product to help you with your design.

We would like to reuse the existing textual content, videos and logo on the current site.

Industry/Entity Type

It Company

Requirements
Must have
• We would like flat design, and we would like the new site to be responsive and SEO-friendly.

We need to have our customer logos on the front page.

We would expect to receive handcrafted and maintainable css and html files as well as any new images created by the designer. The maintainability of these files is essential.
Nice to have
• We prefer a bootstrap-based design.
Should not have
• Our target audience is a technical end user who works in a large enterprise IT organisation, typically in a support or operational role, e.g. applications, operations or infrastructure support.

```html
<!DOCTYPE html>
<html lang="en">
<head>
<meta charset="utf-8">
<title>Tracvenna — Big data analytics</title>
<link rel="stylesheet" href="https://fonts.googleapis.com/css2?family=Overpass:wght@400;800;900&display=swap">
<style>
  :root {
    --ink: #22221a;
    --accent: #0a7ff5;
    --paper: #ffffff;
    --logo-grey: #6a6a6a;
    --logo-dot: #8fb4ec;
  }
  * { margin: 0; padding: 0; box-sizing: border-box; }
  html, body {
    width: 1200px;
    height: 1012px;
    overflow: hidden;
    background: var(--paper);
    font-family: "Overpass", sans-serif;
    color: var(--ink);
  }
  .page { position: relative; width: 1200px; height: 1012px; }

  .brand {
    position: absolute;
    left: 42px;
    top: 22px;
    display: flex;
    align-items: center;
    gap: 10px;
    text-decoration: none;
  }
  .brand-dot {
    width: 22px; height: 22px;
    border-radius: 50%;
    background: var(--logo-dot);
  }
  .brand-name {
    font-size: 48px;
    font-weight: 400;
    color: var(--logo-grey);
    line-height: 1;
  }

  .hero-title {
    position: absolute;
    left: 0; right: 0; top: 0;
    text-align: center;
    font-weight: 900;
    letter-spacing: -0.02em;
  }
  .hero-line {
    position: absolute;
    left: 0; right: 0;
    white-space: nowrap;
    line-height: 1;
  }
  .line-big { top: 122px; font-size: 138px; letter-spacing: -0.035em; }
  .line-analytics { top: 255px; font-size: 188px; letter-spacing: -0.045em; }
  .line-analytics .for { font-size: 88px; letter-spacing: -0.02em; margin-left: 24px; }
  .line-realtime { top: 453px; font-size: 86px; letter-spacing: -0.035em; }
  .line-rootcause { top: 572px; font-size: 86px; letter-spacing: -0.035em; }

  .actions { position: absolute; top: 716px; left: 0; width: 1200px; }
  .action {
    position: absolute;
    top: 0;
    width: 241px;
    height: 90px;
    background: var(--accent);
    color: var(--paper);
    font-weight: 800;
    font-size: 52px;
    letter-spacing: -0.03em;
    text-decoration: none;
    display: flex;
    align-items: center;
    justify-content: center;
    padding-top: 8px;
  }
  .action-features { left: 192px; }
  .action-pricing { left: 479px; }
  .action-download { left: 767px; }
  .trial-note {
    position: absolute;
    top: 98px;
    left: 767px;
    width: 241px;
    text-align: center;
    font-size: 19px;
    color: var(--accent);
  }

  .next-slide {
    position: absolute;
    left: 1148px;
    top: 348px;
  }

  .site-nav {
    position: absolute;
    left: 0; bottom: 0;
    width: 1200px;
    height: 71px;
    background: var(--ink);
  }
  .site-nav a {
    position: absolute;
    top: 0;
    height: 71px;
    display: flex;
    align-items: center;
    transform: translateX(-50%);
    color: var(--paper);
    text-decoration: none;
    font-size: 30px;
    padding-top: 4px;
  }
  .nav-product { left: 309px; }
  .nav-help { left: 597px; }
  .nav-try { left: 891px; }
</style>
</head>
<body>
<div class="page">
  <a class="brand" href="#">
    <span class="brand-dot"></span>
    <span class="brand-name">Tracvenna</span>
  </a>

  <h1 class="hero-title">
    <span class="hero-line line-big">Big data</span>
    <span class="hero-line line-analytics">analytics<span class="for">for</span></span>
    <span class="hero-line line-realtime">real-time system monitoring</span>
    <span class="hero-line line-rootcause">and root cause analysis</span>
  </h1>

  <div class="actions">
    <a class="action action-features" href="#">features</a>
    <a class="action action-pricing" href="#">pricing</a>
    <a class="action action-download" href="#">download</a>
    <p class="trial-note">try it free for 30 days</p>
  </div>

  <a class="next-slide" href="#" aria-label="Next slide">
    <svg width="52" height="94" viewBox="0 0 52 94">
      <circle cx="52" cy="47" r="47" fill="var(--ink)"/>
      <path d="M22 32 L36 47 L22 62" fill="none" stroke="var(--paper)" stroke-width="8" stroke-linecap="square"/>
    </svg>
  </a>

  <nav class="site-nav">
    <a class="nav-product" href="#">Product</a>
    <a class="nav-help" href="#">Help</a>
    <a class="nav-try" href="#">Try and Buy</a>
  </nav>
</div>
</body>
</html>
```